- New restaurant page
- I will like to use this page to advertise and mention the grand opening
- QR brand and logo is well known
- Brightwater Fish & Chicken on Larkmoor Crest
- I attached professional pictures that were taking recently
- Initially i will like the design and the facebook logo and the cover photo. in the cover photo I will include the address, phone number and that you can order on Platewagon, mealnest and Plate wagon
- then I will like professional edit the pictures and include the store info.
- this a link of a similar design that i will like to try out. https://www.facebook.com/qrfishvaldane
- address 3167 S Larkmoor Cr Ave,
Chicago, IL 60592
- phone number 7735104286
- email: info@qrfishandchickenonlarkmoor.example

Target Market(s)

facebook for now.

Industry/Entity Type

resturant

Colors
EB3D1F
EC4F4E
F09395
F8D3D4
FCEDEE

Requirements
Must have
• facebook cover photo with contact info and nice design. pictures to post for the grand opening in nice designs
Nice to have
• look at this for ideas https://www.facebook.com/qrfishvaldane

```html
<!DOCTYPE html>
<html lang="en">
<head>
<meta charset="utf-8">
<title>Brightwater Fish &amp; Chicken – Grand Opening</title>
<link rel="stylesheet" href="https://fonts.googleapis.com/css2?family=Montserrat:wght@500;600;700;800&family=Mr+Dafoe&display=swap">
<style>
:root{
  --red:#EB3D1F;
  --coral:#EC4F4E;
  --rose:#F09395;
  --blush:#F8D3D4;
  --mist:#FCEDEE;
  --paper:#f4eeee;
  --ink:#1d1d1d;
  --stage:#a3a3a3;
  --partner-green:#1f8a4c;
  --partner-orange:#f08a1c;
}
*{box-sizing:border-box;margin:0;padding:0}
html,body{width:1200px;height:1200px;overflow:hidden}
body{background:var(--stage);font-family:"Montserrat",sans-serif;color:var(--ink);position:relative}

.cover,.post{position:absolute;background:var(--paper);overflow:hidden;box-shadow:0 6px 18px rgba(0,0,0,.18)}
.cover{left:40px;top:50px;width:1120px;height:415px}
.post{left:290px;top:520px;width:620px;height:620px}

.waves{position:absolute;inset:0;width:100%;height:100%}

.brand-tab{position:absolute;background:#fff;border-radius:0 0 14px 14px;box-shadow:0 4px 12px rgba(0,0,0,.15);display:flex;flex-direction:column;align-items:center;justify-content:center;gap:8px}
.brand-dot{width:14px;height:14px;border-radius:50%;background:var(--red);display:block}
.brand-name{color:var(--ink);font-weight:700;letter-spacing:.01em}
.cover .brand-tab{left:73px;top:0;width:112px;height:100px}
.cover .brand-name{font-size:14px}
.post .brand-tab{left:470px;top:0;width:120px;height:105px}
.post .brand-name{font-size:15px}

.script{position:absolute;font-family:"Mr Dafoe",cursive;color:var(--ink);line-height:1}
.headline{position:absolute;color:var(--red);font-weight:800;line-height:1.05;letter-spacing:.01em;
  text-shadow:2px 2px 0 #fff,5px 5px 0 rgba(235,61,31,.22)}
.cover .script{left:80px;top:118px;font-size:76px}
.cover .headline{left:80px;top:165px;font-size:50px;white-space:nowrap}
.post .script{left:40px;top:40px;font-size:72px}
.post .headline{left:40px;top:92px;font-size:46px}

.info{position:absolute}
.address{font-weight:700;font-size:15px;line-height:1.3}
.line{display:flex;align-items:center;gap:10px;color:var(--red);font-weight:700}
.line svg{flex:none}
.phone{font-size:20px;margin-top:18px}
.email{font-size:13px;margin-top:12px;font-weight:600}
.cover .info{left:108px;top:232px}
.post .info{left:40px;top:215px}
.post .address{font-size:13px}
.post .phone{font-size:18px;margin-top:12px}
.post .email{font-size:11px;margin-top:8px}

.order-btn{position:absolute;background:var(--red);color:#fff;font-weight:700;font-size:14px;letter-spacing:.04em;border-radius:24px;display:flex;align-items:center;justify-content:center;box-shadow:0 3px 8px rgba(235,61,31,.35)}
.cover .order-btn{left:400px;top:243px;width:134px;height:34px}
.post .order-btn{left:40px;top:335px;width:140px;height:34px;font-size:13px}

.partners{position:absolute;display:flex;align-items:center;gap:14px;font-weight:700}
.partner{display:flex;align-items:center;gap:6px}
.partner-a{color:var(--partner-green)}
.partner-b{color:var(--partner-orange)}
.partner-b i{width:11px;height:11px;border-radius:50%;background:var(--partner-orange);display:block}
.cover .partners{left:400px;top:310px;font-size:15px}
.post .partners{left:40px;top:580px;font-size:14px}

.photo{position:absolute;border-radius:50%;border:7px solid var(--red);box-shadow:0 6px 14px rgba(0,0,0,.25)}
.photo-burger{background:radial-gradient(circle at 45% 40%,#d9a25c 0 28%,#8a4b2e 42%,#c83b22 55%,#e8e1c8 70%,#fafafa 100%)}
.photo-wings{background:radial-gradient(circle at 50% 45%,#d9542a 0 40%,#b8361a 60%,#e6c27a 85%,#f3efe6 100%)}
.photo-shrimp{background:radial-gradient(circle at 50% 50%,#e9b54a 0 45%,#d08a2c 70%,#f5f0e4 100%)}
.photo-steak{background:radial-gradient(circle at 50% 50%,#7a5a3c 0 25%,#d7c08a 45%,#e9a14a 65%,#f2ead8 100%)}

.cover .photo-burger{left:798px;top:15px;width:265px;height:265px}
.cover .photo-wings{left:612px;top:140px;width:200px;height:200px}
.cover .photo-shrimp{left:790px;top:292px;width:125px;height:125px}
.cover .photo-steak{left:963px;top:200px;width:215px;height:215px}

.post .photo-burger{left:345px;top:128px;width:260px;height:260px}
.post .photo-wings{left:200px;top:362px;width:180px;height:180px}
.post .photo-steak{left:400px;top:402px;width:225px;height:225px}
</style>
</head>
<body>

<section class="cover" aria-label="Facebook cover – Grand Opening">
  <svg class="waves" viewBox="0 0 1120 415" preserveAspectRatio="none" aria-hidden="true">
    <defs>
      <linearGradient id="coverWave" x1="0" y1="0" x2="1" y2="1">
        <stop offset="0" stop-color="#F09395"/>
        <stop offset=".45" stop-color="#EC4F4E"/>
        <stop offset="1" stop-color="#EB3D1F"/>
      </linearGradient>
    </defs>
    <path d="M450 0 L1120 0 L1120 415 L900 415 C860 330 780 300 720 250 C650 190 690 110 600 70 C540 40 500 12 450 0 Z" fill="url(#coverWave)"/>
    <path d="M0 330 C150 330 250 415 390 415 L0 415 Z" fill="url(#coverWave)"/>
    <path d="M0 360 C140 360 220 415 300 415 L0 415 Z" fill="#F8D3D4" opacity=".55"/>
  </svg>

  <div class="brand-tab"><i class="brand-dot"></i><span class="brand-name">Brightwater</span></div>

  <div class="script">The</div>
  <h1 class="headline">GRAND OPENING</h1>

  <div class="info">
    <p class="address">3167 S Larkmoor Cr Ave,<br>Chicago, IL 60592</p>
    <p class="line phone">
      <svg width="22" height="22" viewBox="0 0 24 24" aria-hidden="true"><path fill="currentColor" d="M6.6 10.8a15.1 15.1 0 0 0 6.6 6.6l2.2-2.2c.3-.3.7-.4 1-.2 1.1.4 2.3.6 3.6.6.6 0 1 .4 1 1V20c0 .6-.4 1-1 1A17 17 0 0 1 3 4c0-.6.4-1 1-1h3.5c.6 0 1 .4 1 1 0 1.3.2 2.5.6 3.6.1.3 0 .7-.2 1z"/></svg>
      7735104286
    </p>
    <p class="line email">
      <svg width="20" height="20" viewBox="0 0 24 24" aria-hidden="true"><circle cx="12" cy="12" r="11" fill="currentColor"/><path d="M6 8h12v8H6z" fill="#fff"/><path d="M6 8l6 5 6-5" fill="none" stroke="currentColor" stroke-width="1.4"/></svg>
      info@qrfishandchickenonlarkmoor.example
    </p>
  </div>

  <div class="order-btn">ORDER NOW</div>

  <div class="partners">
    <span class="partner partner-a">Platewagon</span>
    <span class="partner partner-b"><i></i>Mealnest</span>
  </div>

  <div class="photo photo-burger" role="img" aria-label="Photo of a roast beef burger with tomato and lettuce"></div>
  <div class="photo photo-wings" role="img" aria-label="Photo of fried chicken wings with fries"></div>
  <div class="photo photo-shrimp" role="img" aria-label="Photo of fried shrimp"></div>
  <div class="photo photo-steak" role="img" aria-label="Photo of a cheesesteak sandwich with fries"></div>
</section>

<section class="post" aria-label="Grand Opening post">
  <svg class="waves" viewBox="0 0 620 620" preserveAspectRatio="none" aria-hidden="true">
    <defs>
      <linearGradient id="postWave" x1="0" y1="0" x2="1" y2="1">
        <stop offset="0" stop-color="#F09395"/>
        <stop offset=".5" stop-color="#EC4F4E"/>
        <stop offset="1" stop-color="#EB3D1F"/>
      </linearGradient>
    </defs>
    <path d="M330 0 L620 0 L620 620 L470 620 C430 560 400 500 430 420 C460 330 360 280 380 180 C395 100 340 40 330 0 Z" fill="url(#postWave)"/>
    <path d="M0 560 C100 560 180 620 260 620 L0 620 Z" fill="url(#postWave)"/>
  </svg>

  <div class="brand-tab"><i class="brand-dot"></i><span class="brand-name">Brightwater</span></div>

  <div class="script">The</div>
  <h2 class="headline">GRAND<br>OPENING</h2>

  <div class="info">
    <p class="address">3167 S Larkmoor Cr Ave,<br>Chicago, IL 60592</p>
    <p class="line phone">
      <svg width="18" height="18" viewBox="0 0 24 24" aria-hidden="true"><path fill="currentColor" d="M6.6 10.8a15.1 15.1 0 0 0 6.6 6.6l2.2-2.2c.3-.3.7-.4 1-.2 1.1.4 2.3.6 3.6.6.6 0 1 .4 1 1V20c0 .6-.4 1-1 1A17 17 0 0 1 3 4c0-.6.4-1 1-1h3.5c.6 0 1 .4 1 1 0 1.3.2 2.5.6 3.6.1.3 0 .7-.2 1z"/></svg>
      7735104286
    </p>
    <p class="line email">
      <svg width="16" height="16" viewBox="0 0 24 24" aria-hidden="true"><circle cx="12" cy="12" r="11" fill="currentColor"/><path d="M6 8h12v8H6z" fill="#fff"/><path d="M6 8l6 5 6-5" fill="none" stroke="currentColor" stroke-width="1.4"/></svg>
      info@qrfishandchickenonlarkmoor.example
    </p>
  </div>

  <div class="order-btn">ORDER NOW</div>

  <div class="partners">
    <span class="partner partner-a">Platewagon</span>
    <span class="partner partner-b"><i></i>Mealnest</span>
  </div>

  <div class="photo photo-burger" role="img" aria-label="Photo of a roast beef burger with tomato and lettuce"></div>
  <div class="photo photo-wings" role="img" aria-label="Photo of fried chicken wings with fries"></div>
  <div class="photo photo-steak" role="img" aria-label="Photo of a cheesesteak sandwich with fries"></div>
</section>

</body>
</html>
```